Emerging Australian photographer

I'm based in Cunderdin, a small rural town in the Wheatbelt area of Western Australia. So its a good thing that I love to travel further afield both for pleasure and for work. To me that is one and the same thing in any event!

My desire is to take photos that make the viewers heart skip. I love taking photos of people doing the things they love or being with the people they love. For me, the joy of photography comes with capturing the 'moments between the moments'. I like candid photography best of all - like when the new husband is staring joyfully at his bride and at that minute is unaware of the photographer capturing the moment.

I am available for weddings, engagements, birthdays, special events, newborns, family or individual portraits. By the end of the year I will be accredited with the Coastal Guild of Image Artisans.

I need a card that stands out but is elegant and would sit well on the table at a wedding or be given out in the church grounds. Classy and a little bit sassy.

Target Market(s)

Consumers who are seeking photographic services, eg wedding guests who see me at work and make enquiries.

Industry/Entity Type

Church

Contact Information for Business Card

Tamsin Bexley Photography
Tamsin Bexley
0452 307 618
www.tamsinbexley.com.au
photos@tamsinbexley.com.au

Requirements
Must have
• Must fit with the theme in the watermarks, but be crisp and modern.
Nice to have
• However it's not essential to have the pink! Facebook and Twitter logos.
Should not have
• Old style fonts like times new roman.

```html
<!DOCTYPE html>
<html lang="en">
<head>
<meta charset="utf-8">
<title>Tamsin Bexley Photography – Business Card</title>
<link rel="stylesheet" href="https://fonts.googleapis.com/css2?family=Raleway:wght@300&display=swap">
<style>
  :root {
    --backdrop: #1c1a1a;
    --card-top: #3a3a3c;
    --card-bottom: #2a2a2c;
    --ink-grey: #a6a6a8;
    --ink-soft: #8c8c8e;
    --ink-pink: #d9a3b8;
    --heart-pink: #f2b6cc;
  }
  * { box-sizing: border-box; margin: 0; padding: 0; }
  html, body {
    width: 1200px;
    height: 800px;
    overflow: hidden;
    background: var(--backdrop);
  }
  .canvas {
    width: 1200px;
    height: 800px;
    display: flex;
    align-items: center;
    justify-content: center;
    gap: 60px;
    font-family: "Raleway", sans-serif;
    font-weight: 300;
  }
  .card {
    width: 520px;
    height: 318px;
    border-radius: 4px;
    background: radial-gradient(ellipse at 45% 40%, var(--card-top), var(--card-bottom) 75%);
    box-shadow: 0 12px 30px rgba(0,0,0,0.45);
    position: relative;
  }
  .card-front {
    display: flex;
    align-items: center;
    justify-content: center;
  }
  .brand {
    display: flex;
    align-items: center;
    gap: 12px;
    color: var(--ink-grey);
    font-size: 30px;
    letter-spacing: 0.5px;
    text-transform: lowercase;
  }
  .brand-dot {
    width: 10px;
    height: 10px;
    border-radius: 50%;
    background: var(--heart-pink);
    flex: none;
  }
  .card-back {
    padding: 38px 44px;
    display: flex;
    flex-direction: column;
  }
  .card-back .brand {
    font-size: 22px;
    margin-bottom: 40px;
  }
  .contact {
    list-style: none;
    display: flex;
    flex-direction: column;
    gap: 10px;
    font-size: 16px;
  }
  .contact-name {
    color: var(--ink-soft);
    font-size: 24px;
    margin-bottom: 4px;
  }
  .contact-phone,
  .contact-email { color: var(--ink-pink); }
  .contact-web { color: var(--ink-pink); }
</style>
</head>
<body>
  <main class="canvas">
    <section class="card card-front" aria-label="Card front">
      <div class="brand">
        <span class="brand-dot"></span>
        <span class="brand-name">tamsin bexley photography</span>
      </div>
    </section>
    <section class="card card-back" aria-label="Card back">
      <div class="brand">
        <span class="brand-dot"></span>
        <span class="brand-name">tamsin bexley photography</span>
      </div>
      <ul class="contact">
        <li class="contact-name">Tamsin Bexley</li>
        <li class="contact-phone">0452 307 618</li>
        <li class="contact-web">www.tamsinbexley.com.au</li>
        <li class="contact-email">photos@tamsinbexley.com.au</li>
      </ul>
    </section>
  </main>
</body>
</html>
```